Cafe Menu Required

We need a menu for our coffee shop.
I would like something very much the same as what I have attached.

I have attached a word doc with the items needed on the menu.

I have also attached our logo

I would like to print these on A3 size poster

Industry/Entity Type

Cafe

```html
<!DOCTYPE html>
<html lang="en">
<head>
<meta charset="UTF-8">
<title>Nova Corner Canteen – Menu</title>
<link href="https://fonts.googleapis.com/css2?family=Arimo:wght@400;700&family=Open+Sans:wght@600;700&display=swap" rel="stylesheet">
<style>
  :root {
    --frame-red: #e91e45;
    --band-red: #ed1c24;
    --panel: #dde2d8;
    --ink: #222222;
    --strip: #1f1f1f;
    --backdrop: #d4d4d4;
    --white: #ffffff;
  }
  * { margin: 0; padding: 0; box-sizing: border-box; }
  html, body { width: 870px; height: 1200px; overflow: hidden; }
  body { background: var(--backdrop); position: relative; font-family: "Arimo", Arial, sans-serif; color: var(--ink); }

  .poster { position: absolute; left: 37px; top: 37px; width: 796px; height: 1126px; background: var(--frame-red); }
  .side-strips { position: absolute; left: 0; top: 0; }
  .panel { position: absolute; left: 36px; top: 36px; width: 724px; height: 1052px; background: var(--panel); }

  .tagline-band { position: absolute; left: 263px; top: 148px; width: 533px; height: 37px; background: var(--frame-red); }
  .tagline { position: absolute; left: 314px; top: 153px; font-family: "Open Sans", Arial, sans-serif; font-weight: 600; font-size: 20px; letter-spacing: 0.6px; color: var(--ink); white-space: nowrap; }

  .brand-disc { position: absolute; left: 68px; top: 58px; width: 198px; height: 198px; border-radius: 50%; background: var(--white); border: 6px solid var(--frame-red); }
  .brand-name { position: absolute; left: 68px; top: 58px; width: 198px; height: 198px; display: flex; align-items: center; justify-content: center; font-family: "Open Sans", Arial, sans-serif; font-weight: 700; font-size: 58px; color: var(--frame-red); letter-spacing: 1px; }

  .menu-column { position: absolute; top: 308px; width: 328px; }
  .menu-column.left { left: 54px; }
  .menu-column.right { left: 402px; }
  .divider { position: absolute; left: 393px; top: 308px; width: 2px; height: 652px; background: #8c8c8c; }

  .section-title { text-align: center; font-weight: 700; font-size: 16px; height: 18px; margin-bottom: 60px; }
  .section-title.spaced { margin-top: 44px; }
  .item { display: flex; align-items: baseline; height: 39px; font-size: 16px; }
  .item .leader { flex: 1; margin: 0 4px; border-bottom: 2px dotted #444; transform: translateY(-4px); }
  .item .price { white-space: nowrap; }

  .social-band { position: absolute; left: 36px; top: 1003px; width: 724px; height: 85px; background: var(--band-red); display: flex; align-items: center; justify-content: center; }
  .social-text { font-size: 34px; color: var(--ink); }
</style>
</head>
<body>
  <div class="poster">
    <div class="panel"></div>
    <svg class="side-strips" width="796" height="1126" viewBox="0 0 796 1126">
      <polygon points="0,410 36,398 36,1006 0,1016" fill="#1f1f1f"/>
      <polygon points="760,185 796,185 796,770 760,783" fill="#1f1f1f"/>
    </svg>

    <div class="tagline-band"></div>
    <div class="tagline">COFFEE – CATERING – FOOD TO GO</div>

    <div class="brand-disc"></div>
    <div class="brand-name">NOVA</div>

    <div class="menu-column left">
      <h2 class="section-title">HOT BEVERAGES</h2>
      <div class="item"><span>Espresso</span><span class="leader"></span><span class="price">3.5</span></div>
      <div class="item"><span>Piccolo</span><span class="leader"></span><span class="price">3.5</span></div>
      <div class="item"><span>Short Macchiato</span><span class="leader"></span><span class="price">4.0</span></div>
      <div class="item"><span>Long Macchiato</span><span class="leader"></span><span class="price">4.5</span></div>
      <div class="item"><span>Latte</span><span class="leader"></span><span class="price">4/4.5/5.5</span></div>
      <div class="item"><span>Cappucinno</span><span class="leader"></span><span class="price">4/4.5/5.5</span></div>
      <div class="item"><span>Flat White</span><span class="leader"></span><span class="price">4/4.50/5.50</span></div>
      <div class="item"><span>Long Black</span><span class="leader"></span><span class="price">4/4.50/5.50</span></div>
      <div class="item"><span>Hot Chocolate</span><span class="leader"></span><span class="price">4/4.50/5.50</span></div>
      <div class="item"><span>White Hot Chocolate</span><span class="leader"></span><span class="price">4/4.50/5.50</span></div>
      <div class="item"><span>Mocha</span><span class="leader"></span><span class="price">4.5/5.0/6.0</span></div>
      <div class="item"><span>White Choc Mocha</span><span class="leader"></span><span class="price">4.5/5.0/6.0</span></div>
      <div class="item"><span>Chai Latte</span><span class="leader"></span><span class="price">4.5/5.0/6.0</span></div>
      <div class="item"><span>Dirty Chai</span><span class="leader"></span><span class="price">5.0/5.5/6.5</span></div>
      <div class="item"><span>Selection of Teas</span><span class="leader"></span><span class="price">3.8</span></div>
    </div>

    <div class="divider"></div>

    <div class="menu-column right">
      <h2 class="section-title">EXTRAS</h2>
      <div class="item"><span>Extra Shot</span><span class="leader"></span><span class="price">0.5</span></div>
      <div class="item"><span>Decaf</span><span class="leader"></span><span class="price">0.5</span></div>
      <div class="item"><span>Syrups – Caramel/Hazelnut/Vanilla</span><span class="leader"></span><span class="price">0.5</span></div>
      <div class="item"><span>Soy</span><span class="leader"></span><span class="price">0.5</span></div>
      <div class="item"><span>Lactose free</span><span class="leader"></span><span class="price">0.5</span></div>
      <h2 class="section-title spaced">COLD BEVERAGES</h2>
      <div class="item"><span>Iced Latte</span><span class="leader"></span><span class="price">4.5</span></div>
      <div class="item"><span>Iced Long Black</span><span class="leader"></span><span class="price">4.5</span></div>
      <div class="item"><span>Iced Coffee w/ice cream</span><span class="leader"></span><span class="price">6.0</span></div>
      <div class="item"><span>Iced Chocolate w/ice cream</span><span class="leader"></span><span class="price">6.0</span></div>
      <div class="item"><span>Coffee Frappe</span><span class="leader"></span><span class="price">6.0</span></div>
      <div class="item"><span>Mango Frappe</span><span class="leader"></span><span class="price">6.0</span></div>
    </div>

    <div class="social-band">
      <p class="social-text">Your social media links here</p>
    </div>
  </div>
</body>
</html>
```